Visitenkarten-Design für klassischen Bauernhof
Vielen Dank für die tolle Zusammenarbeit Henrike. Die Visitenkarten sind genau so wie wir sie uns vorgestellt haben. Jederzeit gerne wieder :) LG Ulrike
Liebe Designer,
wir sind ein klassicher Bauernhof mit Ziegen und Direktvermarktung (SB-Hofladen).
Informationen über die Visitenkarten sind unter 'Vorgaben' aufgelistet.
Vielen Dank!
NACHTRAG - VIELEN HERZLICHEN DANK AN ALLE GRAFIKER FÜR DIE UNZÄHLIGEN WIRKLICH RESTLOS TOLLEN DESIGNS!!
DAS WAR KEINE LEICHTE ENTSCHEIDUNG...
Aufgabenstellung
Folgende Angaben sollten auf der Visitenkarte enthalten sein:
Ziegenhof Brunnrieth (Logo)
SB Hofladen täglich geöffnet
Hofkäserei
Die Visitenkarten kann gerne auch beidseitig bedruckt werden.
Eine Zeile um ggf. eine Mobilfunknummer eintragen zu können wäre praktisch aber nicht dringend notwendig (ebenso ein Ziegenbild)

```html
<!DOCTYPE html>
<html lang="de">
<head>
<meta charset="utf-8">
<title>Ziegenhof Brunnrieth – Visitenkarten</title>
<link href="https://fonts.googleapis.com/css2?family=Maven+Pro:wght@400;600&display=swap" rel="stylesheet">
<style>
  :root{
    --sheet:#ffffff;
    --card:#e4e5de;
    --brown:#5a2f1e;
    --green:#0b8f3c;
    --white:#ffffff;
    --photo-a:#6b4a33;
    --photo-b:#d9d4cc;
  }
  html,body{margin:0;padding:0;overflow:hidden;}
  body{width:848px;height:1200px;background:var(--sheet);position:relative;
       font-family:"Maven Pro",Arial,sans-serif;}
  .card{position:absolute;top:205px;width:337px;height:217px;background:var(--card);
        box-shadow:3px 3px 4px rgba(0,0,0,.25);overflow:hidden;}
  .card--front{left:67px;}
  .card--back{left:430px;}

  /* Front */
  .front-mark{position:absolute;left:118px;top:30px;width:96px;height:96px;border-radius:50%;
              border:2px solid var(--green);box-sizing:border-box;
              background:radial-gradient(circle at 50% 45%,#c9bfb2 0%,var(--card) 70%);}
  .front-name{position:absolute;left:0;right:0;top:140px;text-align:center;
              font-size:22px;font-weight:600;color:var(--brown);line-height:1.1;}

  /* Back */
  .back-art{position:absolute;left:0;top:0;}
  .back-name{position:absolute;left:20px;top:18px;font-size:15px;font-weight:600;
             color:var(--brown);line-height:1.1;width:120px;}
  .contact{position:absolute;left:169px;top:23px;color:var(--brown);font-size:10px;line-height:15px;}
  .contact__person{font-weight:600;font-size:11.5px;}
  .contact__gap{height:6px;}
  .badge-text{position:absolute;left:56px;width:76px;text-align:center;color:var(--white);line-height:1.1;}
  .badge-text--shop{top:141px;font-size:9.5px;}
  .badge-text--cheese{top:179px;font-size:9px;}
  .social{position:absolute;left:12px;top:182px;color:var(--white);font-size:9px;font-weight:600;}
  .web{position:absolute;left:169px;top:183px;color:var(--white);font-size:11px;font-weight:600;}
</style>
</head>
<body>

<section class="card card--front">
  <div class="front-mark" role="img" aria-label="Platz für Hofzeichen: Ziege auf Wiese mit Ähren"></div>
  <div class="front-name">Ziegenhof<br>Brunnrieth</div>
</section>

<section class="card card--back">
  <svg class="back-art" width="337" height="217" viewBox="0 0 337 217">
    <defs>
      <linearGradient id="photoTone" x1="0" y1="0" x2="1" y2="1">
        <stop offset="0" stop-color="var(--photo-a)"/>
        <stop offset=".5" stop-color="var(--photo-b)"/>
        <stop offset="1" stop-color="var(--photo-a)"/>
      </linearGradient>
    </defs>
    <circle cx="72" cy="133" r="74" fill="url(#photoTone)" role="img"
            aria-label="Foto: weiße Ziegen schauen über die Stallbox"/>
    <polygon class="band" points="0,177 337,156 337,217 0,217" fill="var(--green)"/>
    <circle cx="94" cy="168" r="38" fill="none" stroke="var(--white)" stroke-width="1"/>
    <line x1="60" y1="170" x2="128" y2="170" stroke="none"/>
  </svg>

  <div class="back-name">Ziegenhof<br>Brunnrieth</div>

  <div class="contact">
    <div class="contact__person">Familie Berger</div>
    <div>Brunnriethweg 4</div>
    <div>77880 Lindenau</div>
    <div>(Post: 77862 Lindenau-Oberfeld)</div>
    <div class="contact__gap"></div>
    <div>T. 07851-462</div>
    <div>M. 0170-9876543</div>
    <div>F. 07851-917</div>
    <div>info@ziegenhof-brunnrieth.de</div>
  </div>

  <div class="badge-text badge-text--shop">SB Hofladen<br>täglich geöffnet</div>
  <div class="badge-text badge-text--cheese">Hofkäserei</div>

  <div class="social">Hofnetz</div>
  <div class="web">www.ziegenhof-brunnrieth.de</div>
</section>

</body>
</html>
```